Architectural Design Build company needs a direct mail flyer

We are a fully service Design Build company who specialize in luxury custom and pre-designed new homes and major home renovations. Our team consists of seasoned architectural, interior design and general contracting professionals all under one roof. We offer clients a transparent, streamlined process to maximize their investment and completion on a timely basis. Leveraging photography and a few before and after and also our Best Builder Awards.

Target Market(s)

Homeowners and buyers between 40-60 years old and financial investment of $300k or more for renovations and $1,000,000 or more for new construction.

Industry/Entity Type

homebuilding and renovations

Colors

Designer to choose colors to be used in the design.

Requirements
Must have
• The construction segments we are focusing this mailer on are transformative renovations and professionally designed custom new homes. . Should have the Pelbrook Before kitchen and after as well as the exterior before and after. and new construction elevation photos.
Nice to have
• WOuld like to see two befores and afters highlighted, mention that are architect and designer are part of the team from start to finish,

```html
<!DOCTYPE html>
<html lang="en">
<head>
<meta charset="utf-8">
<title>Pelbrook Design Build – Direct Mail Flyer</title>
<link rel="stylesheet" href="https://fonts.googleapis.com/css2?family=Poppins:wght@400;500;600;700&family=Oswald:wght@500;600&family=Playfair+Display:wght@400&display=swap">
<style>
:root{
  --lime:#b8d432;
  --ink:#1c1c1c;
  --paper:#ffffff;
  --stage:#e4e4e4;
  --muted:#2b2b2b;
}
*{box-sizing:border-box;margin:0;padding:0}
html,body{width:1200px;height:796px;overflow:hidden}
body{background:var(--stage);font-family:"Poppins",sans-serif;color:var(--ink);position:relative}
.page{position:absolute;top:65px;width:479px;height:619px;background:var(--paper);overflow:hidden}
.page--front{left:98px}
.page--back{left:623px}
.abs{position:absolute}
.layer{position:absolute;left:0;top:0}

/* brand */
.brand{left:26px;top:24px;display:flex;align-items:center;gap:12px}
.brand__name{font-family:"Poppins",sans-serif;font-weight:700;font-size:23px;letter-spacing:.5px;color:var(--ink);text-transform:uppercase}
.brand__tag{font-size:8px;font-weight:500;letter-spacing:2.4px;color:var(--ink)}

/* hero */
.hero__title{left:24px;top:78px;font-family:"Playfair Display",serif;font-size:45px;line-height:1;color:var(--lime);letter-spacing:1px}
.hero__sub{left:24px;top:124px;font-family:"Oswald",sans-serif;font-weight:500;font-size:30px;line-height:1;color:#fff;letter-spacing:.3px}
.hero__tagline{left:25px;top:160px;font-size:16px;line-height:1.12;color:#fff}

/* ribbons */
.ribbon{position:absolute;display:flex;align-items:center;justify-content:center;font-family:"Poppins",sans-serif;font-weight:700;color:var(--ink);text-transform:uppercase}
.ribbon--process{left:146px;top:227px;width:184px;height:19px;font-size:12.5px}
.ribbon--timeline{left:146px;top:461px;width:184px;height:22px;font-size:13.5px}
.ribbon--about{left:100px;top:26px;width:150px;height:27px;font-size:14px;justify-content:flex-start;padding-left:35px}

/* text blocks */
.h-green{font-weight:600;color:var(--lime);text-transform:uppercase;line-height:1.15}
.h-green--md{font-size:10.5px}
.h-green--lg{font-size:12.5px}
.h-green--sm{font-size:10px}
.h-black{font-weight:500;font-size:8.3px;line-height:1.2;color:var(--ink)}
.h-caps{font-weight:600;font-size:7.8px;text-transform:uppercase;color:var(--ink)}
.body{font-size:5.6px;line-height:1.32;color:var(--muted)}
.body + .body{margin-top:5px}
.mt2{margin-top:2px}.mt4{margin-top:4px}.mt6{margin-top:6px}.mt8{margin-top:8px}

.checks{list-style:none;margin-top:6px}
.checks li{position:relative;padding-left:9px;font-size:5.5px;line-height:1.3;color:var(--muted);margin-bottom:2.4px}
.checks li::before{content:"";position:absolute;left:0;top:1px;width:5px;height:5px;border-radius:50%;background:var(--lime)}
.checks li::after{content:"";position:absolute;left:1.6px;top:2.1px;width:1.3px;height:2.2px;border:solid #fff;border-width:0 .8px .8px 0;transform:rotate(40deg)}

/* timeline */
.step{position:absolute;width:30px;height:30px;border-radius:50%;background:var(--lime);border:2.5px solid var(--ink);display:flex;align-items:center;justify-content:center;font-family:"Oswald",sans-serif;font-weight:500;font-size:16px;color:var(--ink);box-shadow:0 2px 2px rgba(0,0,0,.35)}
.step-label{position:absolute;width:80px;margin-left:-40px;text-align:center;font-size:5.2px;font-weight:700;line-height:1.25;text-transform:uppercase;color:var(--ink)}
.step-label span{display:block;font-weight:400;text-transform:none;font-size:5.4px}

/* footer */
.footer{position:absolute;left:0;bottom:0;width:479px;height:41px}
.footer__contact{position:absolute;left:26px;top:3px;line-height:1.1}
.footer__label{font-weight:500;font-size:10.5px;color:var(--ink)}
.footer__phone{display:flex;align-items:center;gap:3px;font-size:10.5px;color:var(--ink)}
.footer__links{position:absolute;top:13px;right:24px;display:flex;align-items:center;gap:4px;font-size:9.6px;white-space:nowrap;color:#fff}
.footer__links .ico{display:inline-flex}
.footer__links .ico--web{margin-left:6px}

/* photos */
.photo{position:absolute}

/* about */
.about__text{left:135px;top:62px;width:172px}
.about__text .body{color:#e8e8e8;font-size:5.4px}
.about__owners{left:135px;top:182px}
.about__owners .role{font-size:6px;color:var(--lime)}
.about__owners .names{font-size:5.3px;color:#fff;text-transform:uppercase;margin-top:2px}
.ba-label{position:absolute;font-size:7.5px;font-weight:600}
.ba-label--before{color:var(--ink)}
.ba-label--after{color:var(--lime)}

.badge{position:absolute;top:313px;width:56px;height:89px;background:var(--ink)}
</style>
</head>
<body>

<!-- FRONT PAGE -->
<section class="page page--front">
  <svg class="layer" width="479" height="619" viewBox="0 0 479 619" aria-hidden="true">
    <polygon points="0,62 248,62 170,225 0,225" fill="var(--ink)"/>
    <polygon points="266,22 280,22 184,225 170,225" fill="var(--lime)"/>
  </svg>
  <svg class="layer" width="479" height="619" viewBox="0 0 479 619" role="img" aria-label="Photo of a white two-storey craftsman custom home with a front porch and lawn">
    <defs>
      <linearGradient id="homeTone" x1="0" y1="0" x2="0" y2="1">
        <stop offset="0" stop-color="#dfe6ec"/>
        <stop offset=".62" stop-color="#c9ccc9"/>
        <stop offset=".78" stop-color="#6f8f3e"/>
        <stop offset="1" stop-color="#4f7a2a"/>
      </linearGradient>
    </defs>
    <polygon points="280,22 479,22 479,225 184,225" fill="url(#homeTone)"/>
  </svg>

  <div class="abs brand"><span class="brand__name">Pelbrook</span><span class="brand__tag">DESIGN BUILD</span></div>
  <div class="abs hero__title">LUXURY</div>
  <div class="abs hero__sub">CUSTOM HOMES</div>
  <div class="abs hero__tagline">Building Dreams<br>Transforming lives</div>

  <svg class="layer" width="479" height="619" viewBox="0 0 479 619" aria-hidden="true">
    <polygon points="150,227 334,227 328,246 144,246" fill="var(--lime)"/>
    <polygon points="150,461 334,461 328,483 144,483" fill="var(--lime)"/>
  </svg>
  <div class="ribbon ribbon--process">The Pelbrook Process</div>

  <div class="abs" style="left:24px;top:263px;width:208px">
    <h3 class="h-green h-green--md">Designed to maximize investment</h3>
    <p class="h-black mt2">From construction to completion</p>
    <p class="body mt4">Our approach begins with a thorough consultation to understand the client's specific needs, preferences, and budget. This allows us to create a preliminary design tailored to the client's vision, along with an initial cost estimate.</p>
    <p class="body">Throughout the project, our interior design team remains involved, providing input and refining the design as needed.</p>
    <p class="h-black mt6">Due diligence to identify key considerations before design</p>
    <p class="body mt2">Before diving into design, we guide our client through essential preparatory steps, such as</p>
    <ul class="checks">
      <li>Compliance with local jurisdiction (city and county requirements such as zoning, flood, height and other restrictions</li>
      <li>HOA, Architectural or other quasi-judicial requirements</li>
      <li>Wetland, Soil and Geotechnical Evaluations</li>
      <li>Zoning Restrictions</li>
      <li>Easements</li>
    </ul>
  </div>

  <div class="abs" style="left:250px;top:263px;width:204px">
    <h3 class="h-green h-green--md">The Design-Build Team</h3>
    <p class="h-black mt2">Architect</p>
    <p class="body mt2">Our Architect collaborates closely with the entire team to ensure seamless design integration, bringing together the interior design, cost, and construction teams to create a cohesive vision for your home.</p>
    <p class="h-black mt6">Interior designer</p>
    <p class="body mt2">Our Interior Design team works alongside the architect to meet your aesthetic and functional goals with materials selections.</p>
    <p class="h-black mt8">Preconstruction manager</p>
    <p class="body mt2">The Preconstruction team provides accurate cost projections based on current market trends, aligning your design vision with your budget through innovative solutions.</p>
    <p class="h-black mt8">Construction manager</p>
    <p class="body mt2">Our Construction team builds your home with precision and quality.</p>
  </div>

  <div class="ribbon ribbon--timeline">Design-Build Timeline</div>

  <div class="step-label" style="left:43px;top:486px">Initial<br>Consultation<span>(1-2 weeks)</span></div>
  <div class="step-label" style="left:147px;top:496px">Design Development<span>(1-2 months)</span></div>
  <div class="step-label" style="left:266px;top:494px">Permitting<span>(1-3 months)</span></div>
  <div class="step-label" style="left:372px;top:494px">Final Inspection<span>(1-4 weeks)</span></div>

  <div class="step" style="left:28px;top:514px">01</div>
  <div class="step" style="left:79px;top:514px">02</div>
  <div class="step" style="left:132px;top:514px">03</div>
  <div class="step" style="left:191px;top:514px">04</div>
  <div class="step" style="left:251px;top:514px">05</div>
  <div class="step" style="left:305px;top:514px">06</div>
  <div class="step" style="left:357px;top:514px">07</div>
  <div class="step" style="left:411px;top:514px">08</div>

  <div class="step-label" style="left:94px;top:551px">Schematic Design<span>(1-2 months)</span></div>
  <div class="step-label" style="left:206px;top:551px;width:100px;margin-left:-50px">Construction Documents<span>(1 month)</span></div>
  <div class="step-label" style="left:320px;top:552px">Construction<span>(5-16 months)</span></div>
  <div class="step-label" style="left:426px;top:552px">Post Completion<br>Support<span>(12 months)</span></div>

  <footer class="footer">
    <svg class="layer" width="479" height="41" viewBox="0 0 479 41" aria-hidden="true">
      <rect width="479" height="41" fill="var(--ink)"/>
      <polygon points="0,0 142,0 162,41 0,41" fill="var(--lime)"/>
    </svg>
    <div class="footer__contact">
      <div class="footer__label">Contact Us Today</div>
      <div class="footer__phone">
        <svg width="9" height="9" viewBox="0 0 10 10" aria-hidden="true"><circle cx="5" cy="5" r="5" fill="var(--ink)"/><path d="M3.3 2.6l1 1-.5.7c.4.8 1 1.4 1.8 1.8l.7-.5 1 1-.6.8C5 7.3 2.7 5 2.5 3.2z" fill="var(--lime)"/></svg>
        813-555-0142
      </div>
    </div>
    <div class="footer__links">
      <span class="ico"><svg width="9" height="9" viewBox="0 0 10 10" aria-hidden="true"><circle cx="5" cy="5" r="5" fill="var(--lime)"/><rect x="2.4" y="3.2" width="5.2" height="3.6" fill="none" stroke="var(--ink)" stroke-width=".7"/><path d="M2.4 3.2L5 5.3l2.6-2.1" fill="none" stroke="var(--ink)" stroke-width=".7"/></svg></span>
      <span>designsolutions@pelbrook.com</span>
      <span class="ico ico--web"><svg width="9" height="9" viewBox="0 0 10 10" aria-hidden="true"><circle cx="5" cy="5" r="5" fill="var(--lime)"/><circle cx="5" cy="5" r="2.8" fill="none" stroke="var(--ink)" stroke-width=".6"/><path d="M2.2 5h5.6M5 2.2v5.6" stroke="var(--ink)" stroke-width=".6"/></svg></span>
      <span>www.pelbrook.com</span>
    </div>
  </footer>
</section>

<!-- BACK PAGE -->
<section class="page page--back">
  <svg class="layer" width="479" height="619" viewBox="0 0 479 619" aria-hidden="true">
    <rect x="0" y="53" width="313" height="146" fill="var(--ink)"/>
    <polygon points="100,26 244,26 258,53 100,53" fill="var(--lime)"/>
  </svg>
  <div class="ribbon ribbon--about">About Us</div>

  <div class="photo" style="left:17px;top:23px;width:112px;height:200px;background:linear-gradient(180deg,#3a3a3a 0%,#2a2a2a 55%,#4a5a70 75%,#2c3440 100%)" role="img" aria-label="Photo of the two company owners standing side by side in black shirts"></div>

  <div class="abs about__text">
    <p class="body">At Pelbrook, our success is driven by the exceptional talent and dedication of our team. Led by owners Dorian Vale, M. Eng., and Marcus Henley—both esteemed former pro football players— our diverse team brings together a wealth of experience and expertise.</p>
    <p class="body">As a design/build company, Pelbrook seamlessly integrates design and construction services. This collaborative model ensures transparent communication, streamlined workflows, and efficient problem solving throughout the project lifecycle. Clients benefit from a holistic and cohesive approach to their project, resulting in superior quality, cost-effectiveness, and timely delivery.</p>
  </div>
  <div class="abs about__owners">
    <div class="role">OWNERS</div>
    <div class="names">Dorian Vale, M. Eng. and Marcus Henley</div>
  </div>

  <span class="ba-label ba-label--before" style="left:333px;top:50px">BEFORE</span>
  <span class="ba-label ba-label--after" style="left:404px;top:50px">AFTER</span>
  <div class="photo" style="left:324px;top:60px;width:54px;height:61px;background:linear-gradient(160deg,#9aa0a2,#4b4f52)" role="img" aria-label="Kitchen before renovation with dark counters"></div>
  <div class="photo" style="left:393px;top:60px;width:60px;height:61px;background:linear-gradient(160deg,#f0ece6,#b99a7c)" role="img" aria-label="Kitchen after renovation with white island and pendant lights"></div>
  <div class="photo" style="left:324px;top:134px;width:54px;height:64px;background:linear-gradient(180deg,#c9d6df 0%,#8c9a86 55%,#4e7a30 100%)" role="img" aria-label="Home exterior before renovation"></div>
  <div class="photo" style="left:393px;top:134px;width:60px;height:64px;background:linear-gradient(180deg,#dbe5ec 0%,#d8d8d6 55%,#5d8a33 100%)" role="img" aria-label="Home exterior after renovation in white"></div>
  <span class="ba-label ba-label--before" style="left:333px;top:203px">BEFORE</span>
  <span class="ba-label ba-label--after" style="left:404px;top:203px">AFTER</span>

  <div class="abs" style="left:25px;top:230px;width:220px">
    <h3 class="h-green h-green--lg">Resilient homes built<br>to endure</h3>
    <p class="body mt4">In regions like Florida and Colorado, where extreme weather is a constant challenge, Pelbrook Design Build sets itself apart with its expertise in resilient construction. By focusing on reinforced foundations and materials that exceed building codes, Pelbrook creates homes that combine energy efficiency, durability, and architectural elegance.</p>
    <p class="body mt6">From hurricane-resistant roofing and moisture-proof materials in Florida to insulated siding and framing designed for Colorado's harsh winters, every detail is thoughtfully engineered to withstand the elements. PelbrookStrong represents the perfect balance of strength, efficiency, and design, ensuring that each home remains a secure and timeless investment.</p>
    <h3 class="h-green h-green--sm mt8">At Pelbrook, we build<br>custom luxury homes<br>and spaces perfectly aligned<br>with your unique vision.</h3>
    <p class="h-caps mt6">Building Dreams</p>
    <p class="body mt2">Our clients are not just investing in structures, but in their dreams, aspirations, and legacies. Pelbrook specializes in new home builds, transformative renovations, and select commercial ventures.</p>
    <p class="h-caps mt6">Transforming Lives</p>
    <p class="body mt2">We create spaces that not only reflect our clients' unique lifestyles but also foster a sense of belonging and connection. Whether you're blazing a new trail or reimagining the old, we're ready to collaborate every step of the way.</p>
    <p class="h-caps mt6">Never the same thing twice</p>
    <p class="body mt2">From the unconventional to the ambitious, we embrace a no-limits attitude—building whatever our clients can imagine, and then some.</p>
  </div>

  <div class="photo" style="left:270px;top:231px;width:179px;height:76px;background:linear-gradient(180deg,#8fa6b8 0%,#6d7c86 45%,#b9b2a6 75%,#7a6a58 100%)" role="img" aria-label="Waterfront balcony with outdoor lounge seating and glass railing"></div>

  <div class="badge" style="left:271px" role="img" aria-label="Award badge"></div>
  <div class="badge" style="left:331px" role="img" aria-label="Award badge"></div>
  <div class="badge" style="left:390px" role="img" aria-label="Award badge"></div>

  <div class="abs" style="left:270px;top:414px;width:184px">
    <h3 class="h-green h-green--lg" style="font-size:11.5px">Real estate professional<br>partners program</h3>
    <p class="body mt6">Realtors looking to provide exceptional homes for their clients will find a valuable partner in Pelbrook Design Build. Pelbrook brings a unique advantage with their integrated team of in-house interior designers, architects, and general contractors, ensuring a seamless approach to crafting homes that not only meet but exceed expectations.</p>
    <p class="body">By staying on top of the top-selling features and design trends, Pelbrook tailors each home to align with both buyer demands and the local market. Our commitment to resilient construction goes beyond standard codes, guaranteeing that homes are built to withstand changing environmental conditions and maintain long-term value.</p>
  </div>

  <footer class="footer">
    <svg class="layer" width="479" height="41" viewBox="0 0 479 41" aria-hidden="true">
      <rect width="479" height="41" fill="var(--ink)"/>
      <polygon points="0,0 137,0 155,41 0,41" fill="var(--lime)"/>
    </svg>
    <div class="footer__contact">
      <div class="footer__label">Contact Us Today</div>
      <div class="footer__phone">
        <svg width="9" height="9" viewBox="0 0 10 10" aria-hidden="true"><circle cx="5" cy="5" r="5" fill="var(--ink)"/><path d="M3.3 2.6l1 1-.5.7c.4.8 1 1.4 1.8 1.8l.7-.5 1 1-.6.8C5 7.3 2.7 5 2.5 3.2z" fill="var(--lime)"/></svg>
        813-555-0142
      </div>
    </div>
    <div class="footer__links">
      <span class="ico"><svg width="9" height="9" viewBox="0 0 10 10" aria-hidden="true"><circle cx="5" cy="5" r="5" fill="var(--lime)"/><rect x="2.4" y="3.2" width="5.2" height="3.6" fill="none" stroke="var(--ink)" stroke-width=".7"/><path d="M2.4 3.2L5 5.3l2.6-2.1" fill="none" stroke="var(--ink)" stroke-width=".7"/></svg></span>
      <span>designsolutions@pelbrook.com</span>
      <span class="ico ico--web"><svg width="9" height="9" viewBox="0 0 10 10" aria-hidden="true"><circle cx="5" cy="5" r="5" fill="var(--lime)"/><circle cx="5" cy="5" r="2.8" fill="none" stroke="var(--ink)" stroke-width=".6"/><path d="M2.2 5h5.6M5 2.2v5.6" stroke="var(--ink)" stroke-width=".6"/></svg></span>
      <span>www.pelbrook.com</span>
    </div>
  </footer>
</section>

</body>
</html>
```